Dermot's Lager BEER CAN

DESIGN USE
This is not for a business, it's for a (thoughtful) gift to my father. The design is going to be on a personalised beer can, so it will be a cylindrical shape. Basically, I'm giving him a few six-packs with his own beer label. I've attached the copy and put design specs below.
RATIONALE
My Dad is a cool guy, one of life’s absolute gems. He’s not a big drinker, but he likes a beer and he’s more likely to give them away at Christmas time than keep them in the fridge and drink them himself.
He’s also a master of Dad Jokes and offering pearls of wisdom, so combining a good beer with a funny Dad Joke or two on a can will be a great gift to give him for his birthday, Father’s Day or Christmas.
PLACEMENT
The front of the can needs to be my Dad’s head in cartoon form and DERMOT’S LAGER has to be the most prominent wording.
While DERMOT’S LAGER is the main heading…I’d like A BRAMBLE RIDGE BREW up the top and DERMOT’S LAGER IS LIFE’S BEER NECESSITY as the key wording wrapping around the bottom of the can.
I'd also like these sayings/jokes included (all of them OR as many that look cool and don't make the design too crowded):
“A beer in each hand is a balanced diet,” - Dermot

“This beer tastes like I’m not going to work tomorrow,” - Dermot

“Your beer isn’t half-full…it’s halfway to your next brew,” - Dermot

“My doc says I shouldn’t drink every day…that’s why I tend to drink at night,” - Dermot

“Two beer or not two beer,” - Shakesbeer

Why do frogs taste like beer?
Because of all the hops

What does Uncle Nev drink?
A polar beer
Why do we like beer?
Coz you can’t drink bacon

Fat? Nah, beer makes you lean…
…against walls, doors…hotties

What's a beer’s favourite language?
Hebrew
DESIGN
Use the photos as a guide to turn my Dad (Dermot) into a cartoon - smiling/grinning, upbeat and happy. Not too old looking!
In terms of the can’s design, this is where I want YOU to be a design maestro. His head could burst through DERMOT’S LAGER or simply have the lettering wrapped around his image.
Are the quotes and jokes in speech bubbles? Or are they in beer bubbles? Is a smaller version of Dad’s head used as a bullet point by each quote or joke?
FONT
Your choice! It just needs to be easy to read or and not too old-fashioned or - at the other extreme - too futuristic.
COLOUR
Your choice! He’s from a province that has red and black as their core colours, but if that doesn’t work, please go with a light teal/blue - or some other semi-masculine colour - and a dark colouring for the wording/lettering.
FORMAT
The approved copy needs to be provided as a PDF and a jpeg.
DIMENSIONS
160mm wide by 85mm high.

Target Market(s)

A target market of ONE - my Dad. I want him to LOVE his gift - his own personal beer can with his image and name on it.

Industry/Entity Type

Beer...

Colors

Requirements
Must have
• A fun, impactful BEER CAN design featuring my Dad's cartoon visage and some if not all of the Dad Jokes/beer sayings provided.

```html
<!DOCTYPE html>
<html lang="en">
<head>
<meta charset="utf-8">
<title>Dermot's Lager — Can Label</title>
<link rel="stylesheet" href="https://fonts.googleapis.com/css2?family=Roboto+Condensed:wght@400;700&family=Archivo:wght@600;800&display=swap">
<style>
  :root {
    --can-red: #b0262a;
    --can-red-deep: #7c1517;
    --gold: #a88a3c;
    --label-white: #f2f2f2;
    --ink: #141414;
    --ink-soft: #3a3a3a;
    --tagline-yellow: #e8c42a;
    --portrait-grey: #9a9a9a;
  }
  * { box-sizing: border-box; margin: 0; padding: 0; }
  html, body {
    width: 1200px; height: 1163px; overflow: hidden;
    background: #ffffff;
  }
  .label {
    position: relative;
    width: 1200px; height: 1163px;
    overflow: hidden;
  }
  .label-art { position: absolute; inset: 0; }

  .brand-header {
    position: absolute;
    left: 350px; top: 250px; width: 500px;
    text-align: center;
    font-family: "Archivo", sans-serif;
    color: var(--ink);
  }
  .brew-line {
    font-weight: 600;
    font-size: 20px;
    letter-spacing: 2px;
  }
  .brand-name {
    margin-top: 10px;
    font-weight: 800;
    font-size: 64px;
    line-height: 1;
    letter-spacing: 1px;
  }

  .portrait {
    position: absolute;
    left: 455px; top: 440px;
    width: 290px; height: 370px;
    background: linear-gradient(180deg, #bdbdbd 0%, var(--portrait-grey) 60%, #6e6e6e 100%);
  }

  .sayings, .jokes {
    position: absolute;
    top: 455px;
    list-style: none;
    font-family: "Roboto Condensed", sans-serif;
    color: var(--ink-soft);
    font-size: 15px;
    line-height: 1.2;
  }
  .sayings { left: 120px; width: 310px; }
  .jokes { left: 780px; width: 300px; }
  .sayings li, .jokes li { margin-bottom: 20px; }
  .sayings .credit, .jokes .punchline { font-weight: 700; color: var(--ink); }
  .jokes .punchline { display: block; }

  .tagline {
    position: absolute;
    left: 0; top: 880px; width: 1200px;
    text-align: center;
    font-family: "Archivo", sans-serif;
    font-weight: 600;
    font-size: 24px;
    color: var(--tagline-yellow);
    letter-spacing: 0.2px;
  }
</style>
</head>
<body>
<main class="label">
  <svg class="label-art" width="1200" height="1163" viewBox="0 0 1200 1163" aria-hidden="true">
    <defs>
      <linearGradient id="canRed" x1="0" y1="0" x2="1" y2="0">
        <stop offset="0" stop-color="#7c1517"/>
        <stop offset="0.35" stop-color="#b0262a"/>
        <stop offset="0.65" stop-color="#c13035"/>
        <stop offset="1" stop-color="#7c1517"/>
      </linearGradient>
      <linearGradient id="labelFill" x1="0" y1="0" x2="1" y2="0">
        <stop offset="0" stop-color="#d4d4d4"/>
        <stop offset="0.4" stop-color="#f2f2f2"/>
        <stop offset="1" stop-color="#b8b8b8"/>
      </linearGradient>
      <clipPath id="shieldClip">
        <polygon points="600,200 1110,450 1110,820 600,1040 90,820 90,450"/>
      </clipPath>
    </defs>
    <rect class="can-body" width="1200" height="1163" fill="url(#canRed)"/>
    <polygon class="shield-rim" points="600,150 1160,425 1160,845 600,1090 40,845 40,425" fill="var(--gold)"/>
    <polygon class="shield-face" points="600,200 1110,450 1110,820 600,1040 90,820 90,450" fill="url(#labelFill)"/>
    <g clip-path="url(#shieldClip)">
      <rect class="lower-band" x="0" y="830" width="1200" height="333" fill="var(--ink)"/>
    </g>
  </svg>

  <header class="brand-header">
    <p class="brew-line">A BRAMBLE RIDGE BREW</p>
    <h1 class="brand-name">DERMOT’S<br>LAGER</h1>
  </header>

  <div class="portrait" role="img" aria-label="Cartoon portrait of Dermot, smiling, wearing glasses"></div>

  <ul class="sayings">
    <li>“A beer in each hand is a balanced diet,” - <span class="credit">Dermot</span></li>
    <li>“This beer tastes like I’m not going to work tomorrow,” - <span class="credit">Dermot</span></li>
    <li>“Your beer isn’t half-full…it’s halfway to your next brew,” - <span class="credit">Dermot</span></li>
    <li>“My doc says I shouldn’t drink every day…that’s why I tend to drink at night,” - <span class="credit">Dermot</span></li>
    <li>“Two beer or not two beer,” - <span class="credit">Shakesbeer</span></li>
  </ul>

  <ul class="jokes">
    <li>Why do frogs taste like beer?<span class="punchline">Because of all the hops</span></li>
    <li>What does Uncle Nev drink?<span class="punchline">A polar beer</span></li>
    <li>Why do we like beer?<span class="punchline">Coz you can’t drink bacon</span></li>
    <li>Fat? Nah, beer makes you lean…<span class="punchline">…against walls, doors…hotties</span></li>
    <li>What’s a beer’s favourite language?<span class="punchline">Hebrew</span></li>
  </ul>

  <p class="tagline">DERMOT’S LAGER IS LIFE’S BEER NECESSITY</p>
</main>
</body>
</html>
```